Folded Business Cards for Guarantee, Layaway & The Fine Print

I am looking for a set of (3) folded business for our guarantee, layaway and fine print policies. I would like the same design for each of these cards, with the exception of the picture, title and verbiage.
The front of each card must include our logo, the title of the card (Our Guarantee, Layaway or The Fine Print,) and a picture of a piece of jewelry. The inside of the card should state our policies. The back of the card should have our logo, address (Bellstone Court #9, Millbrook, VT 05901,) phone # (555-281-0947) email & web address (info@vantorgems.com, www.vantorgems.com) and social media icons (FB, Twitter, Pinterest, Instagram)

The layaway card needs a place for the customer's signature.

I was thinking the orientation of the card should be vertical but if the right design ends up being horizontal, I'm ok with that. I do have concerns about readability and that this may be too much information for a folded business card. So, I am open to either changing the front & back, if need be or going to a different format (standard postcard size. Verbiage may also need to be trimmed down, but I need to know what is possible first.

Our branding colors are espresso brown & coppery orange so please do not stray from this color palette. The font of our logo is joefin. I would like the verbiage of the cards to be in quattrocento sans font. We would like a modern & clean look please.

Attached, please find our logo, policies and jewelry pictures. For picture placement, please do the following: Layaway Card (Quartz & onyx pendant,) The Fine Print Card (Orange Garnet Pendant,) Our Guarantee (triple Green Tourmaline Ring.)

```html
<!DOCTYPE html>
<html lang="en">
<head>
<meta charset="utf-8">
<title>Vantor Jewelry – Our Guarantee Card</title>
<link rel="stylesheet" href="https://fonts.googleapis.com/css2?family=Josefin+Sans:wght@300&family=Quattrocento+Sans:wght@400;700&display=swap">
<style>
  :root {
    --page-bg: #ffffff;
    --card-black: #0d0c0b;
    --frame-line: #6a6460;
    --copper: #c8884e;
    --copper-deep: #b5612a;
    --tan: #d9b07c;
    --band-dark: #161514;
    --band-mid: #242220;
    --gem-green: #1f5a33;
    --gold: #b98a3a;
    --divider: #3e3a37;
  }
  * { margin: 0; padding: 0; box-sizing: border-box; }
  html, body {
    width: 1200px; height: 772px; overflow: hidden;
    background: var(--page-bg);
  }
  .sheet { position: relative; width: 1200px; height: 772px; }

  .card {
    position: absolute; top: 133px;
    width: 370px; height: 556px;
    border-radius: 30px;
    background: var(--card-black);
    overflow: hidden;
  }
  .card-front { left: 167px; }
  .card-inside { left: 620px; }

  .card-frame {
    position: absolute; inset: 12px;
    border: 1px solid var(--frame-line);
    border-radius: 22px;
    pointer-events: none; z-index: 3;
  }

  /* front */
  .brand-name {
    position: absolute; left: 0; right: 0; top: 86px;
    text-align: center;
    font-family: "Quattrocento Sans", sans-serif; font-weight: 400;
    font-size: 40px; line-height: 1;
    color: var(--copper);
  }

  .pattern-band {
    position: absolute; left: 0; right: 0; top: 184px; height: 216px;
    background: linear-gradient(180deg, var(--band-dark), var(--band-mid) 50%, var(--band-dark));
  }
  .showcase-ring {
    position: absolute; left: 112px; top: 210px;
    width: 146px; height: 146px; border-radius: 50%;
    border: 1px solid #3c3936;
  }
  .product-photo {
    position: absolute; left: 129px; top: 254px;
    width: 104px; height: 93px; border-radius: 10px;
    background: radial-gradient(circle at 60% 45%, var(--gem-green) 0 30%, var(--gold) 55%, #3a2c14 100%);
  }
  .card-title {
    position: absolute; left: 0; right: 0; top: 462px;
    text-align: center;
    font-family: "Josefin Sans", sans-serif; font-weight: 300;
    font-size: 27px; color: var(--copper);
  }

  /* inside */
  .policy {
    position: absolute; left: 28px; right: 28px; top: 52px;
    text-align: center; color: var(--copper-deep);
    font-family: "Quattrocento Sans", sans-serif;
  }
  .policy-heading {
    font-family: "Josefin Sans", sans-serif; font-weight: 300;
    font-size: 29px; color: var(--copper); margin-bottom: 24px;
  }
  .policy-item { font-size: 12.5px; line-height: 16px; margin-bottom: 9px; }
  .contact-divider {
    position: absolute; left: 112px; width: 147px; top: 446px;
    border-top: 1px solid var(--divider);
  }
  .contact {
    position: absolute; left: 0; right: 0; top: 470px;
    text-align: center; font-family: "Quattrocento Sans", sans-serif;
    color: var(--copper-deep); font-size: 10.5px; line-height: 13px;
  }
  .contact-address {
    position: absolute; left: 0; right: 0; top: 516px;
    text-align: center; font-family: "Quattrocento Sans", sans-serif;
    color: var(--tan); font-size: 12.5px;
  }
</style>
</head>
<body>
<main class="sheet">

  <section class="card card-front">
    <div class="card-frame"></div>
    <div class="brand-name">Vantor</div>
    <div class="pattern-band" role="img" aria-label="Dark damask pattern band"></div>
    <div class="showcase-ring"></div>
    <div class="product-photo" role="img" aria-label="Photo of a gold ring set with a green tourmaline"></div>
    <h2 class="card-title">our guarantee</h2>
  </section>

  <section class="card card-inside">
    <div class="card-frame"></div>
    <div class="policy">
      <h1 class="policy-heading">Our Promise to You</h1>
      <p class="policy-item">We will repair or replace any piece of jewelry that is determined to be defective in materials and/or workmanship.</p>
      <p class="policy-item">We will repair or replace any stone loss up to 0.20ct per stone, due to defects in materials and/or workmanship.</p>
      <p class="policy-item">Our jewelry repairs are guaranteed for 6 months from completion date.</p>
      <p class="policy-item">Our watch repairs are guaranteed for 90 days from completion date. We do not warranty watches against water damage.</p>
      <p class="policy-item">We offer free lifetime cleaning &amp; inspection of your jewelry from Vantor's. We'll make sure everything is safe &amp; secure and, of course, sparkling. You should do this at least every six months.</p>
      <p class="policy-item">Above all, we want you to be pleased with your jewelry purchase or repair from Vantor's. If you have any questions or concerns, please never hesitate to speak to us.</p>
    </div>
    <div class="contact-divider"></div>
    <div class="contact">
      <div>phone : 555-281-0947</div>
      <div>info@vantorgems.com</div>
      <div>www.vantorgems.com</div>
    </div>
    <div class="contact-address">Bellstone Court #9, Millbrook, VT 05901</div>
  </section>

</main>
</body>
</html>
```